Harbourline Gas and Plumbing Business Card Design

I am after a business card design for my plumbing business called 'Harbourline Gas & Plumbing'. I do all types of plumbing and gas work and specialise in general maintenance plumbing. Would like to see designs using current logo

Industry/Entity Type

Plumbing

Contact Information for Business Card

Name - Dallas McTavish
Phone number - 0468305917
Email - admin@harbourlinegasandplumbing.com.au
ABN - 58104629375

```html
<!DOCTYPE html>
<html lang="en">
<head>
<meta charset="utf-8">
<title>Harbourline Gas &amp; Plumbing – Business Card</title>
<link rel="stylesheet" href="https://fonts.googleapis.com/css2?family=Saira+Semi+Condensed:wght@700&family=Lato:wght@300;400&display=swap">
<style>
  :root {
    --backdrop: #2b2b2d;
    --card: #1e1f21;
    --card-edge: #26272a;
    --brand-blue: #1f74d6;
    --accent-orange: #f08a1c;
    --text-light: #e4e4e6;
    --rule: #6a6b70;
    --pattern-dark: #1a1b1d;
    --pattern-warm: #2a2620;
  }
  * { box-sizing: border-box; margin: 0; padding: 0; }
  html, body {
    width: 1200px;
    height: 1108px;
    overflow: hidden;
    background: var(--backdrop);
  }
  .stage {
    position: relative;
    width: 1200px;
    height: 1108px;
    display: flex;
    justify-content: center;
    align-items: center;
    gap: 70px;
  }
  .card {
    position: relative;
    width: 430px;
    height: 700px;
    border-radius: 26px;
    background: var(--card);
    box-shadow: 0 18px 40px rgba(0,0,0,0.45);
    overflow: hidden;
  }

  /* Front */
  .card-front .brand {
    position: absolute;
    top: 150px;
    left: 50px;
    display: flex;
    align-items: center;
    gap: 14px;
  }
  .brand-dot {
    width: 40px;
    height: 40px;
    border-radius: 50%;
    background: var(--brand-blue);
    flex: none;
  }
  .brand-name {
    font-family: "Saira Semi Condensed", sans-serif;
    font-weight: 700;
    font-size: 30px;
    line-height: 1.05;
    text-transform: uppercase;
    color: var(--brand-blue);
    letter-spacing: 0.5px;
  }
  .contact {
    position: absolute;
    left: 0;
    right: 0;
    bottom: 70px;
    text-align: center;
    font-family: "Lato", sans-serif;
    font-weight: 300;
    color: var(--text-light);
  }
  .contact-name {
    font-family: "Saira Semi Condensed", sans-serif;
    font-weight: 700;
    font-size: 28px;
    text-transform: uppercase;
    color: var(--brand-blue);
    letter-spacing: 0.5px;
    margin-bottom: 10px;
  }
  .contact-rule {
    width: 160px;
    height: 1px;
    margin: 0 auto;
    background: var(--rule);
  }
  .contact-line {
    font-size: 19px;
    line-height: 1.45;
    letter-spacing: 0.3px;
  }
  .contact-phone { margin-top: 8px; }
  .contact-email { font-size: 17px; margin-bottom: 8px; }
  .contact-abn { margin-top: 8px; }
  .abn-label { color: var(--accent-orange); }

  /* Back */
  .card-back .pattern {
    position: absolute;
    inset: 0;
    background:
      radial-gradient(ellipse at 30% 40%, var(--pattern-warm) 0%, transparent 60%),
      linear-gradient(160deg, var(--pattern-dark), var(--card-edge));
  }
  .card-back .brand-back {
    position: absolute;
    left: 0;
    right: 0;
    bottom: 80px;
    text-align: center;
    font-family: "Saira Semi Condensed", sans-serif;
    font-weight: 700;
    font-size: 34px;
    line-height: 1.1;
    text-transform: uppercase;
    color: var(--brand-blue);
    letter-spacing: 0.5px;
  }
</style>
</head>
<body>
<main class="stage">
  <section class="card card-front" aria-label="Card front">
    <div class="brand">
      <span class="brand-dot"></span>
      <span class="brand-name">Harbourline<br>Gas &amp; Plumbing</span>
    </div>
    <div class="contact">
      <p class="contact-name">Dallas McTavish</p>
      <div class="contact-rule"></div>
      <p class="contact-line contact-phone">0468305917</p>
      <p class="contact-line contact-email">admin@harbourlinegasandplumbing.com.au</p>
      <div class="contact-rule"></div>
      <p class="contact-line contact-abn"><span class="abn-label">ABN</span> - 58104629375</p>
    </div>
  </section>

  <section class="card card-back" aria-label="Card back">
    <div class="pattern" role="img" aria-label="Faint repeating brand pattern in dark grey and muted amber"></div>
    <p class="brand-back">Harbourline<br>Gas &amp; Plumbing</p>
  </section>
</main>
</body>
</html>
```